(3) Image Sliders for Wordpress Site

We need to update our WP slides on a corporate website. We are an IP communications solution provider to government and enterprises. Our website is www.velunor.com. You can see the existing sliders for size. I like crisp, professional-looking slides (NOT like the ones currently displayed). They shouldn't look like stock art/photos --- they should look original. They should also use current/new artistic methods (i.e. the "latest" concepts in design).

The Images should be JPG format, 946 x 376.

Use colors from logo on website, but don't completely restrict yourself. Photos are OK.

Slide Text:
Slide 1:
Main Message: "Creative solutions for government"
Bulleted text (use any kind of bullet or separator you want):
-Reduce FTE costs and eliminate capital expenses
-Dramatically improve community services
-Make government accessible for all constituents on all devices

Slide 2:
Main Message: "Corvane Systems Deployment"
-Take advantage of dramatic cost savings vs. going direct
-Leverage VeLUNOR's 13 years of experience
-Deploy On-Premises for optimal security, control and customization

Slide 3:
Main Message: "Enterprise Unified Communications"
-Revolutionize the way your people communicate and collaborate
-Realize instant cost savings by replacing multiple systems with one unified platform
-Bring everyone together, no matter where they are.

Hi Everyone I appreciate your submissions, but they are full of stock graphics and stuff I could have done..Looking for something more creative and unique to us. Since we're primarily a government/enterprise contractor, it doesn't have to be artsy or cute, but it does need to rise above the typical stock stuff i'm seeing. More information: -The Corvane Systems logo should go on the Corvane Systems-related slide -If you need more relevant logos or images let me know. Here are some slides that I like: http://brelmacraft.com/images/2014/0710-1/unslider.jpg http://brelmacraft.com/images/2014/0710-1/superslides.jpg http://www.tovelpikstudio.com/wp-content/uploads/2012/02/jquerysliders10b.jpg something like this with layered text for our gov slider, but NYC skyline: http://www.tovelpikstudio.com/wp-content/uploads/2012/02/jquerysliders18.jpg

Communications

```html
<!DOCTYPE html>
<html lang="en">
<head>
<meta charset="utf-8">
<title>Corvane Systems Deployment – Slider Concepts</title>
<link rel="stylesheet" href="https://fonts.googleapis.com/css2?family=Raleway:wght@300&family=Open+Sans:wght@400;600;700&family=Nunito+Sans:wght@900&display=swap">
<style>
  :root {
    --page: #ffffff;
    --slate: #2b2b2b;
    --slate-dark: #1f1f1f;
    --lime: #8cc21f;
    --white: #ffffff;
    --rule: rgba(255,255,255,0.22);
    --ocean-top: #0f4a6b;
    --ocean-deep: #082a40;
    --button-blue: #1565c0;
    --dot-dim: #6a6a6a;
  }
  html, body {
    margin: 0;
    width: 977px;
    height: 1200px;
    overflow: hidden;
    background: var(--page);
  }
  .slide {
    position: absolute;
    left: 0;
    width: 946px;
    height: 376px;
    overflow: hidden;
    color: var(--white);
    font-family: "Open Sans", Arial, sans-serif;
  }
  .slide--slate { top: 0; background: var(--slate); }
  .slide--harvest { top: 393px; background: radial-gradient(ellipse at 60% 45%, #4a4a46 0%, #262624 45%, #111 100%); }
  .slide--ocean { top: 786px; background: linear-gradient(180deg, var(--ocean-top) 0%, #0b3a57 55%, var(--ocean-deep) 100%); }

  .slide__backdrop { position: absolute; inset: 0; }

  .slide__title {
    position: absolute;
    left: 54px;
    margin: 0;
    font-family: "Raleway", Arial, sans-serif;
    font-weight: 300;
    font-size: 39px;
    letter-spacing: 0.3px;
    white-space: nowrap;
  }
  .slide--slate .slide__title { top: 78px; color: var(--lime); }
  .slide--harvest .slide__title { top: 484px; top: 91px; color: var(--white); }

  .benefits {
    position: absolute;
    left: 54px;
    margin: 0;
    padding: 0;
    list-style: none;
    font-size: 17.5px;
  }
  .benefits li {
    display: flex;
    align-items: center;
    height: 30px;
    white-space: nowrap;
  }
  .benefits svg { flex: none; margin-right: 9px; }
  .slide--slate .benefits { top: 143px; }
  .slide--harvest .benefits { top: 152px; width: 628px; }
  .slide--harvest .benefits li + li { border-top: 1px solid var(--rule); }
  .slide--ocean .benefits { top: 194px; left: 322px; font-size: 17.5px; }
  .slide--ocean .benefits svg { margin-right: 4px; }

  .cta {
    position: absolute;
    left: 57px;
    display: flex;
    align-items: center;
    justify-content: center;
    font-size: 16px;
    color: var(--white);
    text-decoration: none;
    box-sizing: border-box;
  }
  .cta--outline { top: 259px; width: 154px; height: 36px; border: 1px solid var(--white); }
  .cta--flag {
    top: 271px; width: 154px; height: 36px; padding-right: 12px;
    background: var(--lime);
    clip-path: polygon(0 0, 100% 0, 92% 50%, 100% 100%, 0 100%);
  }
  .cta--pill {
    top: 298px; left: 320px; width: 145px; height: 34px;
    border-radius: 17px; background: var(--button-blue);
    font-weight: 700;
  }

  .pager { position: absolute; top: 336px; left: 829px; }
  .dots { position: absolute; display: flex; gap: 4px; }
  .dots span { width: 9px; height: 9px; border-radius: 50%; background: var(--dot-dim); }
  .dots span.is-active { background: var(--white); }
  .slide--slate .dots, .slide--harvest .dots { top: 340px; left: 884px; }
  .slide--ocean .dots { top: 33px; left: 28px; }

  .headline-bar { position: absolute; left: 325px; top: 47px; width: 5px; height: 137px; background: var(--lime); }
  .headline-stack {
    position: absolute; left: 342px; top: 38px; margin: 0;
    font-family: "Nunito Sans", Arial, sans-serif; font-weight: 900;
    font-size: 48px; line-height: 49px; letter-spacing: -0.5px;
    text-transform: uppercase;
  }
</style>
</head>
<body>

<section class="slide slide--slate">
  <svg class="slide__backdrop" width="946" height="376" aria-hidden="true">
    <polygon points="0,0 230,0 0,210" fill="#262626"/>
    <polygon points="480,0 700,0 520,376 260,376" fill="#2f2f2f"/>
    <polygon points="620,0 946,0 946,260" fill="#313131"/>
    <polygon points="520,376 700,0 760,120 640,376" fill="#282828"/>
    <line x1="700" y1="0" x2="520" y2="376" stroke="#3a3a3a" stroke-width="1"/>
  </svg>
  <h2 class="slide__title">Corvane Systems Deployment</h2>
  <ul class="benefits">
    <li><svg width="18" height="18" viewBox="0 0 18 18"><circle cx="9" cy="9" r="7.5" fill="none" stroke="#fff" stroke-width="1.5"/><circle cx="9" cy="9" r="3.5" fill="#fff"/></svg>Take advantage of dramatic cost savings vs. going direct</li>
    <li><svg width="18" height="18" viewBox="0 0 18 18"><circle cx="9" cy="9" r="7.5" fill="none" stroke="#fff" stroke-width="1.5"/><circle cx="9" cy="9" r="3.5" fill="#fff"/></svg>Leverage VeLUNOR's 13 years of experience</li>
    <li><svg width="18" height="18" viewBox="0 0 18 18"><circle cx="9" cy="9" r="7.5" fill="none" stroke="#fff" stroke-width="1.5"/><circle cx="9" cy="9" r="3.5" fill="#fff"/></svg>Deploy On-Premises for optimal security, control and customization</li>
  </ul>
  <a class="cta cta--outline" href="#">Call to Action</a>
  <svg class="pager" width="36" height="16" viewBox="0 0 36 16" aria-hidden="true"><path d="M9 3 4 8l5 5M23 3l5 5-5 5" fill="none" stroke="#fff" stroke-width="2.4"/></svg>
  <div class="dots"><span></span><span class="is-active"></span><span></span></div>
</section>

<section class="slide slide--harvest">
  <div class="slide__backdrop" role="img" aria-label="Black and white photo of cupped hands holding soil with a green seedling sprouting"></div>
  <h2 class="slide__title">Corvane Systems Deployment</h2>
  <ul class="benefits">
    <li><svg width="18" height="18" viewBox="0 0 18 18"><rect x="1.5" y="2.5" width="13" height="13" rx="3" fill="none" stroke="#fff" stroke-width="1.6"/><path d="M5 9l3 3 8-9" fill="none" stroke="#fff" stroke-width="2"/></svg>Take advantage of dramatic cost savings vs. going direct</li>
    <li><svg width="18" height="18" viewBox="0 0 18 18"><rect x="1.5" y="2.5" width="13" height="13" rx="3" fill="none" stroke="#fff" stroke-width="1.6"/><path d="M5 9l3 3 8-9" fill="none" stroke="#fff" stroke-width="2"/></svg>Leverage VeLUNOR's 13 years of experience</li>
    <li><svg width="18" height="18" viewBox="0 0 18 18"><rect x="1.5" y="2.5" width="13" height="13" rx="3" fill="none" stroke="#fff" stroke-width="1.6"/><path d="M5 9l3 3 8-9" fill="none" stroke="#fff" stroke-width="2"/></svg>Deploy On-Premises for optimal security, control and customization</li>
  </ul>
  <a class="cta cta--flag" href="#">Call to Action</a>
  <svg class="pager" width="36" height="16" viewBox="0 0 36 16" aria-hidden="true"><path d="M9 3 4 8l5 5M23 3l5 5-5 5" fill="none" stroke="#fff" stroke-width="2.4"/></svg>
  <div class="dots"><span></span><span class="is-active"></span><span></span></div>
</section>

<section class="slide slide--ocean">
  <div class="slide__backdrop" role="img" aria-label="Deep blue background with faint columns of falling binary digits"></div>
  <div class="dots"><span></span><span class="is-active"></span><span></span></div>
  <div class="headline-bar"></div>
  <h2 class="headline-stack">Corvane<br>Systems<br>Deployment</h2>
  <ul class="benefits">
    <li><svg width="18" height="18" viewBox="0 0 18 18"><circle cx="9" cy="9" r="8" fill="#fff"/><circle cx="9" cy="9" r="5.6" fill="none" stroke="#0b3a57" stroke-width="1.3"/><path d="M6 9l2.2 2.2L12.5 6.5" fill="none" stroke="#0b3a57" stroke-width="1.8"/></svg>Take advantage of dramatic cost savings vs. going direct</li>
    <li><svg width="18" height="18" viewBox="0 0 18 18"><circle cx="9" cy="9" r="8" fill="#fff"/><circle cx="9" cy="9" r="5.6" fill="none" stroke="#0b3a57" stroke-width="1.3"/><path d="M6 9l2.2 2.2L12.5 6.5" fill="none" stroke="#0b3a57" stroke-width="1.8"/></svg>Leverage VeLUNOR's 13 years of experience</li>
    <li><svg width="18" height="18" viewBox="0 0 18 18"><circle cx="9" cy="9" r="8" fill="#fff"/><circle cx="9" cy="9" r="5.6" fill="none" stroke="#0b3a57" stroke-width="1.3"/><path d="M6 9l2.2 2.2L12.5 6.5" fill="none" stroke="#0b3a57" stroke-width="1.8"/></svg>Deploy On-Premises for optimal security, control and customization</li>
  </ul>
  <a class="cta cta--pill" href="#">Call to Action</a>
</section>

</body>
</html>
```